Book cover design for the book titled "Quieter Under Lanterns."

create a book cover. The book title is, "Quieter Under Lanterns: A Ledger of Harbour Songs Across Mild Winters." The purpose of the book is to create awareness of how childhood trauma is impacting 7 out of 10 adults in the world today and that two-thirds of children will experience neglect and or abuse before their 18th birthday. One victim described that his mental and physical illness resulting from childhood trauma felt like he wa being pulled to the ground, that the force was "quieter under lanterns." The design should be clean and simple and communicate a crisis.

```html
<!DOCTYPE html>
<html lang="en">
<head>
<meta charset="utf-8">
<title>Quieter Under Lanterns – Book Cover Wrap</title>
<link rel="stylesheet" href="https://fonts.googleapis.com/css2?family=Bebas+Neue&family=Carlito&display=swap">
<style>
  :root {
    --backdrop: #262626;
    --paper: #ffffff;
    --ink: #0b0b0b;
    --body-ink: #1a1a1a;
    --accent: #ff5200;
    --accent-deep: #b83a00;
    --accent-pale: #ffc7a8;
    --fold: #e4e4e4;
  }
  * { margin: 0; padding: 0; box-sizing: border-box; }
  html, body {
    width: 1200px;
    height: 1200px;
    overflow: hidden;
    background: var(--backdrop);
  }
  .canvas {
    width: 1200px;
    height: 1200px;
    display: flex;
    align-items: center;
    justify-content: center;
  }
  .cover-wrap {
    display: flex;
    height: 790px;
    box-shadow: 0 14px 50px rgba(0,0,0,0.45);
  }
  .panel { background: var(--paper); height: 790px; }
  .panel svg { display: block; width: 100%; height: 100%; }

  /* Back cover */
  .back-cover {
    width: 540px;
    padding: 70px 64px 0 66px;
  }
  .back-title { display: block; width: 410px; height: 62px; }
  .back-subtitle { display: block; width: 410px; height: 34px; margin-top: 6px; }
  .heading { font-family: "Bebas Neue", "Oswald", sans-serif; fill: var(--ink); }
  .heading .highlight, .accent-fill { fill: var(--accent); }
  .blurb {
    margin-top: 18px;
    font-family: "Carlito", "Calibri", sans-serif;
    font-size: 14.2px;
    line-height: 18.6px;
    color: var(--body-ink);
    text-align: justify;
  }
  .blurb p + p { margin-top: 18px; }

  /* Spine */
  .spine {
    width: 62px;
    border-left: 1px solid var(--fold);
    border-right: 1px solid var(--fold);
  }
  .spine-title { font-family: "Bebas Neue", "Oswald", sans-serif; font-size: 40px; fill: var(--ink); }
  .spine-subtitle { font-family: "Bebas Neue", "Oswald", sans-serif; font-size: 19px; fill: var(--ink); }
  .spine-author { font-family: "Bebas Neue", "Oswald", sans-serif; font-size: 20px; fill: var(--ink); }

  /* Front cover */
  .front-cover { width: 540px; }
  .title-word { font-family: "Bebas Neue", "Oswald", sans-serif; font-size: 320px; }
  .title-dark { fill: var(--ink); }
  .title-accent { fill: var(--accent); }
  .subtitle { font-family: "Bebas Neue", "Oswald", sans-serif; font-size: 96px; fill: var(--ink); }
  .subtitle .highlight { fill: var(--accent); }
  .author-name {
    font-family: "Bebas Neue", "Oswald", sans-serif;
    font-size: 46px;
    letter-spacing: 8px;
    fill: var(--accent);
  }
</style>
</head>
<body>
<main class="canvas">
  <div class="cover-wrap">

    <section class="panel back-cover">
      <svg class="back-title" viewBox="0 0 410 62" aria-label="Quieter Under Lanterns">
        <text class="heading" x="0" y="58" font-size="70" textLength="410" lengthAdjust="spacingAndGlyphs">QUIETER UNDER <tspan class="highlight">LANTERNS</tspan></text>
      </svg>
      <svg class="back-subtitle" viewBox="0 0 410 34" aria-label="A Ledger of Harbour Songs Across Mild Winters">
        <text class="heading" x="0" y="30" font-size="34" textLength="410" lengthAdjust="spacingAndGlyphs">A LEDGER OF <tspan class="highlight">HARBOUR SONGS</tspan> ACROSS MILD WINTERS</text>
      </svg>
      <div class="blurb">
        <p>Lorem ipsum dolor sit amet, consectetur adipiscing elit, sed do eiusmod tempor incididunt ut labore et dolore magna aliqua. Quis ipsum suspendisse ultrices gravida. Risus commodo viverra maecenas accumsan lacus vel facilisis. Lorem ipsum dolor sit amet, consectetur adipiscing elit, sed do eiusmod tempor incididunt ut labore et dolore magna aliqua. Quis ipsum suspendisse ultrices gravida. Risus commodo viverra maecenas accumsan lacus vel facilisis. Lorem ipsum dolor sit amet, consectetur adipiscing elit, sed do eiusmod tempor incididunt ut labore et dolore magna aliqua. Quis ipsum suspendisse ultrices gravida. Risus commodo viverra maecenas accumsan lacus vel facilisis. Lorem ipsum dolor sit amet, consectetur adipiscing elit, sed do eiusmod tempor incididunt ut labore et dolore magna aliqua. Quis ipsum suspendisse ultrices gravida. Risus commodo viverra maecenas accumsan lacus vel facilisis.</p>
        <p>Lorem ipsum dolor sit amet, consectetur adipiscing elit, sed do eiusmod tempor incididunt ut labore et dolore magna aliqua. Quis ipsum suspendisse ultrices gravida. Risus commodo viverra maecenas accumsan lacus vel facilisis. Lorem ipsum dolor sit amet, consectetur adipiscing elit, sed do eiusmod tempor incididunt ut labore et dolore magna aliqua. Quis ipsum suspendisse ultrices gravida. Risus commodo viverra maecenas accumsan lacus vel facilisis. Lorem ipsum dolor sit amet, consectetur adipiscing elit, sed do eiusmod tempor incididunt ut labore et dolore magna aliqua. Quis ipsum suspendisse ultrices gravida. Risus commodo viverra maecenas accumsan lacus vel facilisis.</p>
      </div>
    </section>

    <section class="panel spine">
      <svg viewBox="0 0 60 790" aria-label="Spine: Quieter Under Lanterns, A Ledger of Harbour Songs Across Mild Winters, Author Name">
        <g transform="translate(44 0) rotate(90)">
          <text class="spine-title" x="32" y="30" textLength="245" lengthAdjust="spacingAndGlyphs">QUIETER UNDER <tspan class="accent-fill">LANTERNS</tspan></text>
          <text class="spine-subtitle" x="292" y="20" textLength="278" lengthAdjust="spacingAndGlyphs">A LEDGER OF <tspan class="accent-fill">HARBOUR SONGS</tspan> ACROSS MILD WINTERS</text>
          <text class="spine-author" x="588" y="21" textLength="165" lengthAdjust="spacing">AUTHOR NAME</text>
        </g>
      </svg>
    </section>

    <section class="panel front-cover">
      <svg viewBox="0 0 780 1140" preserveAspectRatio="none" aria-labelledby="cover-title">
        <title id="cover-title">Quieter Under Lanterns: A Ledger of Harbour Songs Across Mild Winters</title>
        <defs>
          <radialGradient id="head-tones" cx="45%" cy="50%" r="60%">
            <stop offset="0%" stop-color="#b83a00"/>
            <stop offset="45%" stop-color="#ff5200"/>
            <stop offset="100%" stop-color="#ffc7a8"/>
          </radialGradient>
        </defs>
        <text class="title-word title-dark" x="50" y="300" textLength="680" lengthAdjust="spacingAndGlyphs">QUIETER</text>
        <text class="title-word title-dark" x="50" y="555" textLength="400" lengthAdjust="spacingAndGlyphs">UND</text>
        <g role="img" aria-label="Illustration in place of the letter E: layered paper-cut human head profiles in graded orange tones">
          <ellipse cx="532" cy="443" rx="68" ry="112" fill="url(#head-tones)"/>
        </g>
        <text class="title-word title-dark" x="606" y="555" textLength="124" lengthAdjust="spacingAndGlyphs">R</text>
        <text class="title-word title-accent" x="50" y="810" textLength="680" lengthAdjust="spacingAndGlyphs">LANTERNS</text>
        <text class="subtitle" x="50" y="925" textLength="680" lengthAdjust="spacingAndGlyphs">A LEDGER OF <tspan class="highlight">HARBOUR SONGS</tspan></text>
        <text class="subtitle" x="110" y="1015" textLength="560" lengthAdjust="spacingAndGlyphs">ACROSS MILD WINTERS</text>
        <text class="author-name" x="390" y="1085" text-anchor="middle">AUTHOR NAME</text>
      </svg>
    </section>

  </div>
</main>
</body>
</html>
```